Mother's Day Sale Banner Ad For Jewelry Site

We are looking for a designer to design a banner on our website advertising our Mother's Day Sale. I have enclosed a few pieces of jewelry we would like used in the ad. The ad size needs to be 1187 × 400. The ad should say:

Mother's Day Sale - Save 15% with Promo Code: LOVEMOM

```html
<!DOCTYPE html>
<html lang="en">
<head>
<meta charset="UTF-8">
<title>Mother's Day Sale Banner</title>
<link rel="stylesheet" href="https://fonts.googleapis.com/css2?family=Marcellus&family=Raleway:wght@200&family=Montserrat:wght@800&display=swap">
<style>
  :root {
    --page-bg: #e4e4e4;
    --banner-white: #ffffff;
    --blush: #f3b8ef;
    --blush-soft: #fbe6fa;
    --mist: #ececec;
    --ink: #575158;
    --magenta: #e11fd3;
    --gold: #cdb46a;
    --silver: #e6e4df;
  }
  * { margin: 0; padding: 0; box-sizing: border-box; }
  html, body {
    width: 1200px;
    height: 619px;
    overflow: hidden;
    background: var(--page-bg);
  }
  .banner {
    position: absolute;
    left: 6px;
    top: 109px;
    width: 1187px;
    height: 400px;
    overflow: hidden;
    background:
      radial-gradient(ellipse 520px 260px at 1000px 260px, var(--mist) 0%, rgba(236,236,236,0) 70%),
      linear-gradient(100deg, var(--blush) 0%, var(--blush-soft) 30%, var(--banner-white) 52%, var(--banner-white) 100%);
  }
  .banner__jewelry {
    position: absolute;
    left: 14px;
    top: 143px;
    width: 590px;
    height: 192px;
    border-radius: 18px;
    background: linear-gradient(180deg, var(--gold) 0%, var(--silver) 20%, var(--silver) 80%, var(--gold) 100%);
  }
  .banner__headline {
    position: absolute;
    right: 36px;
    top: 28px;
    font-family: "Marcellus", serif;
    font-size: 104px;
    line-height: 1;
    color: var(--ink);
    letter-spacing: 1px;
    white-space: nowrap;
  }
  .banner__sale {
    position: absolute;
    right: 40px;
    top: 118px;
    font-family: "Raleway", sans-serif;
    font-weight: 200;
    font-size: 216px;
    line-height: 1;
    color: var(--magenta);
    letter-spacing: 4px;
    white-space: nowrap;
  }
  .banner__offer {
    position: absolute;
    right: 40px;
    top: 329px;
    font-family: "Montserrat", sans-serif;
    font-weight: 800;
    font-size: 30px;
    line-height: 1;
    color: var(--ink);
    white-space: nowrap;
  }
  .banner__code { color: var(--magenta); }
</style>
</head>
<body>
  <section class="banner">
    <div class="banner__jewelry" role="img" aria-label="Three gold and white filigree diamond band rings"></div>
    <h1 class="banner__headline">Mother's DAY</h1>
    <p class="banner__sale">SALE</p>
    <p class="banner__offer">Save 15% with Promo Code: <span class="banner__code">LOVEMOM</span></p>
  </section>
</body>
</html>
```